Cancer Prevention

Heralds' Gardens is hosting a presentation by guest speaker Lena Varkosh, ND regarding cancer prevention April 29th, 2014 from 6:30pm until 7:30pm. There will be snacks and refreshments available during the presentation as well as questions answered following. There will be 3 door prizes given out at the conclusion of the presentation. Please incorporate a few of the pictures provided as well as a description of our speaker which is provided. Card must be 2-sided with the exception of the back right side to allow address and postage. Our address and phone number:
Heralds' Gardens
2745 W 38th St
Tulsa, OK 74119
918-526-3941

Please change the date to April 29th as we have moved the event to that date

We have moved the event to April 29th instead of April 22nd & the RSVP date should be changed to April 22nd. Please make the necessary adjustments to the postcards accordingly. Thank you

Font styles to use
Decorative
Script

Requirements
Must have
• Must have at least 5 or more of the provided photos total. The description of our speaker is also necessary, however if you choose to shorten it that is fine as well.
2-sided postcard with room on back right for address and postage. Must include "call 918-526-3941 to RSVP by April 22nd" somewhere in the card. Also, please include the fact that we will be giving door prizes away.

Heralds' Gardens
2745 W 38th St
Tulsa, OK 74119
918-526-3941
Also, please include placement of RSVP

```html
<!DOCTYPE html>
<html lang="en">
<head>
<meta charset="utf-8">
<title>Heralds' Gardens – Cancer Prevention Postcard (Back)</title>
<link rel="stylesheet" href="https://fonts.googleapis.com/css2?family=EB+Garamond:ital,wght@1,400;1,700&display=swap">
<style>
  :root {
    --frame-start: #5ccbd2;
    --frame-end: #0cb2e8;
    --card-white: #ffffff;
    --rsvp-pink: #e3157f;
    --address-grey: #4a4a4a;
    --divider-grey: #555555;
    --diagram-purple: #7b3f98;
    --diagram-green: #1e7a4e;
    --diagram-blue: #2a6ea8;
    --produce-red: #c4263a;
    --produce-yellow: #f2b21c;
    --produce-green: #5a9a2e;
    --emblem-green: #5bb33a;
    --emblem-dark: #2d7a2a;
  }
  * { margin: 0; padding: 0; box-sizing: border-box; }
  html, body {
    width: 1200px;
    height: 924px;
    overflow: hidden;
    background: #ffffff;
  }
  .postcard-back {
    position: relative;
    width: 1200px;
    height: 924px;
    background: linear-gradient(160deg, var(--frame-start) 0%, var(--frame-end) 100%);
  }
  .card-panel {
    position: absolute;
    left: 28px;
    top: 28px;
    width: 1144px;
    height: 868px;
    background: var(--card-white);
  }
  .rsvp-callout {
    position: absolute;
    left: 60px;
    top: 70px;
    width: 540px;
    text-align: center;
    font-family: "EB Garamond", serif;
    font-style: italic;
    font-weight: 700;
    font-size: 50px;
    line-height: 66px;
    color: var(--rsvp-pink);
  }
  .rsvp-callout sup {
    font-size: 26px;
    vertical-align: 22px;
    line-height: 0;
  }
  .return-address {
    position: absolute;
    left: 60px;
    top: 330px;
    width: 445px;
    text-align: center;
    font-family: "EB Garamond", serif;
    font-style: italic;
    font-weight: 400;
    font-size: 44px;
    line-height: 93px;
    color: var(--address-grey);
    letter-spacing: 1px;
  }
  .mailing-divider {
    position: absolute;
    left: 598px;
    top: 290px;
    width: 4px;
    height: 530px;
    border-left: 3px dotted var(--divider-grey);
  }
  .topic-art {
    position: absolute;
    display: block;
  }
  .prevention-diagram { left: 64px; top: 710px; width: 142px; height: 148px; }
  .produce-wheel { left: 266px; top: 718px; width: 128px; height: 128px; }
  .health-emblem { left: 424px; top: 708px; width: 120px; height: 154px; }
</style>
</head>
<body>
  <main class="postcard-back">
    <section class="card-panel">
      <p class="rsvp-callout">Call 918-526-3941 to<br>RSVP by April 22<sup>nd</sup></p>

      <address class="return-address">
        2745 W 38th St.,<br>
        Tulsa, OK 74119,<br>
        Ph. : 918-526-3941
      </address>

      <div class="mailing-divider" aria-hidden="true"></div>
    </section>

    <svg class="topic-art prevention-diagram" viewBox="0 0 142 148" role="img" aria-label="Cancer prevention diagram linking weight, diet and physical activity">
      <defs>
        <radialGradient id="diagramTone" cx="50%" cy="45%" r="60%">
          <stop offset="0%" stop-color="#6a7fae"/>
          <stop offset="55%" stop-color="var(--diagram-green)"/>
          <stop offset="100%" stop-color="var(--diagram-purple)"/>
        </radialGradient>
      </defs>
      <circle cx="71" cy="74" r="70" fill="url(#diagramTone)"/>
    </svg>

    <svg class="topic-art produce-wheel" viewBox="0 0 128 128" role="img" aria-label="Wheel of colourful fruits and vegetables">
      <defs>
        <linearGradient id="produceTone" x1="0" y1="0" x2="1" y2="1">
          <stop offset="0%" stop-color="#4a3a6a"/>
          <stop offset="35%" stop-color="var(--produce-red)"/>
          <stop offset="65%" stop-color="var(--produce-yellow)"/>
          <stop offset="100%" stop-color="var(--produce-green)"/>
        </linearGradient>
      </defs>
      <circle cx="64" cy="64" r="63" fill="url(#produceTone)"/>
    </svg>

    <svg class="topic-art health-emblem" viewBox="0 0 120 154" role="img" aria-label="Green leafy medical emblem">
      <defs>
        <linearGradient id="emblemTone" x1="0" y1="0" x2="0" y2="1">
          <stop offset="0%" stop-color="var(--emblem-green)"/>
          <stop offset="100%" stop-color="var(--emblem-dark)"/>
        </linearGradient>
      </defs>
      <rect x="0" y="0" width="120" height="154" rx="20" fill="url(#emblemTone)"/>
    </svg>
  </main>
</body>
</html>
```